Business Advisory Firm Business Card

A clean, very upscale looking business card. Not crowded.

Please include logo (attached) and:

Danielle R. Kastrup
Four Ashgrove Court
New York, NY 10087
tel: (917) 555-3140
fax: (646) 555-2973
email: dkastrup@silvermerepartners.example
website: www.silvermerepartners.example

Target Market(s)

Business clients. Often real estate development firms, other advisory firms or growing companies that need assistance. I would like a card that looks impressive and confident.

Industry/Entity Type

Business

Colors

Designer to choose colors to be used in the design.

Requirements
Must have
• Impressive and confident. Please include logo.
Should not have
• nothing flashy...

```html
<!DOCTYPE html>
<html lang="en">
<head>
<meta charset="utf-8">
<title>Silvermere Advisory Partners – Business Card</title>
<link href="https://fonts.googleapis.com/css2?family=Oswald:wght@600&family=Open+Sans:wght@400;600&display=swap" rel="stylesheet">
<style>
  :root {
    --bg-light: #e6e6e6;
    --bg-dark: #bdbdbd;
    --card-white: #ffffff;
    --ink: #1c1c1c;
    --ink-soft: #555555;
    --lime: #9dc01a;
    --lime-bright: #b1cf0a;
    --olive: #6a7d12;
    --steel: #a9a9a9;
  }
  * { box-sizing: border-box; margin: 0; padding: 0; }
  html, body { width: 1200px; height: 1000px; overflow: hidden; }
  body {
    position: relative;
    background: radial-gradient(ellipse at 50% 35%, var(--bg-light) 0%, var(--bg-dark) 100%);
    font-family: "Open Sans", Arial, sans-serif;
  }
  .card {
    position: absolute;
    width: 600px;
    height: 343px;
    box-shadow: 0 12px 28px rgba(0,0,0,0.28);
    overflow: hidden;
  }
  /* Front */
  .card-front { left: 100px; top: 110px; background: var(--card-white); }
  .brand { position: absolute; left: 62px; top: 68px; display: flex; align-items: center; gap: 18px; }
  .brand-square { width: 56px; height: 56px; background: var(--lime); flex: none; }
  .brand-name {
    font-family: "Oswald", "Arial Narrow", sans-serif;
    font-weight: 600;
    font-size: 24px;
    line-height: 1.02;
    text-transform: uppercase;
    color: var(--ink);
  }
  .divider { position: absolute; left: 0; top: 176px; width: 372px; height: 2px; background: var(--ink); }
  .person { position: absolute; left: 384px; top: 150px; }
  .person-name { font-size: 17px; font-weight: 600; color: var(--lime); }
  .person-title { font-size: 12px; color: var(--ink-soft); margin-top: 2px; }
  .contact { position: absolute; left: 40px; top: 196px; font-size: 14px; color: var(--ink); }
  .contact-address { margin-bottom: 6px; }
  .contact-grid { display: grid; grid-template-columns: 150px auto; row-gap: 5px; column-gap: 14px; }
  .contact-item { display: flex; align-items: center; gap: 7px; white-space: nowrap; }
  .icon { width: 13px; height: 13px; flex: none; }
  .accent-line { position: absolute; left: 0; bottom: 40px; width: 100%; height: 4px; background: var(--steel); }
  .accent-band { position: absolute; left: 0; bottom: 0; width: 100%; height: 40px; background: linear-gradient(90deg, var(--olive), var(--lime)); }
  /* Back */
  .card-back {
    left: 500px; top: 540px;
    background: radial-gradient(ellipse at 50% 50%, var(--lime-bright) 0%, var(--olive) 100%);
    display: flex; align-items: center; justify-content: center; gap: 16px;
  }
  .back-square { width: 44px; height: 44px; background: var(--steel); }
  .back-name {
    font-family: "Oswald", "Arial Narrow", sans-serif;
    font-weight: 600;
    font-size: 22px;
    text-transform: uppercase;
    color: var(--card-white);
  }
</style>
</head>
<body>
  <section class="card card-front">
    <div class="brand">
      <div class="brand-square"></div>
      <div class="brand-name">Silvermere<br>Advisory<br>Partners, Inc.</div>
    </div>
    <div class="divider"></div>
    <div class="person">
      <div class="person-name">Danielle R. Kastrup</div>
      <div class="person-title">CEO</div>
    </div>
    <div class="contact">
      <div class="contact-address">Four Ashgrove Court, New York, NY 10087</div>
      <div class="contact-grid">
        <div class="contact-item">
          <svg class="icon" viewBox="0 0 13 13"><rect width="13" height="13" rx="2" fill="var(--lime)"/><path d="M3.5 3h2l.7 2-1 .8a5 5 0 0 0 2 2l.8-1 2 .7v2c-4 .3-6.8-2.5-6.5-6.5z" fill="#fff"/></svg>
          (917) 555-3140
        </div>
        <div class="contact-item">
          <svg class="icon" viewBox="0 0 13 13"><rect width="13" height="13" rx="2" fill="var(--lime)"/><rect x="2.5" y="4" width="8" height="5.5" fill="none" stroke="#fff"/><path d="M2.5 4l4 3 4-3" fill="none" stroke="#fff"/></svg>
          dkastrup@silvermerepartners.example
        </div>
        <div class="contact-item">
          <svg class="icon" viewBox="0 0 13 13"><rect width="13" height="13" rx="2" fill="var(--lime)"/><rect x="4" y="2.5" width="5" height="3" fill="#fff"/><rect x="2.5" y="6" width="8" height="4.5" fill="#fff"/></svg>
          (646) 555-2973
        </div>
        <div class="contact-item">
          <svg class="icon" viewBox="0 0 13 13"><circle cx="6.5" cy="6.5" r="6.5" fill="var(--lime)"/><circle cx="6.5" cy="6.5" r="4" fill="none" stroke="#fff"/><path d="M2.5 6.5h8M6.5 2.5c-2 2.5-2 5.5 0 8M6.5 2.5c2 2.5 2 5.5 0 8" fill="none" stroke="#fff" stroke-width=".8"/></svg>
          www.silvermerepartners.example
        </div>
      </div>
    </div>
    <div class="accent-line"></div>
    <div class="accent-band"></div>
  </section>

  <section class="card card-back">
    <div class="back-square"></div>
    <div class="back-name">Silvermere Advisory Partners</div>
  </section>
</body>
</html>
```